Postcard 4.25"x 6" template

We need a postcard template to send information about our wellness clinic's classes and groups.
The mailing side needs space for changeable text to talk about the clinic and brief info about our classes and groups, in addition to meeting the Federal Letter Carriage Bureau requirements for address and return address area. The return address space can be fixed with our clinic's name and address on it.
The other side should be a dynamic calendar. For the time being, please use the information listed for the month of February. However, this should be changeable so that we can update the month and the events.
Somewhere on the postcard should also be a link to our website's events page:
http://www.torvesihall.com/events
Please work with our website for guidance on the look and feel of our marketing materials.
Overall it should have a natural feel.
It needs to be able to be printed at a regular printing shop and look good. It should not require a large commercial printer.
It will also need to be editable in a Word Document format.

```html
<!DOCTYPE html>
<html lang="en">
<head>
<meta charset="utf-8">
<title>Dynamic Calendar – February 2014 – Torvesi Hall</title>
<link rel="stylesheet" href="https://fonts.googleapis.com/css2?family=Arimo:wght@700&family=Roboto+Condensed:wght@400&family=Questrial&display=swap">
<style>
  :root {
    --paper: #e4eadc;
    --sage: #6f8a55;
    --title-green: #6a8a55;
    --leaf-green: #5cc552;
    --white: #ffffff;
  }
  * { margin: 0; padding: 0; box-sizing: border-box; }
  html, body { width: 1200px; height: 859px; overflow: hidden; background: var(--paper); }
  .calendar-card {
    position: relative;
    width: 1200px;
    height: 859px;
    background: var(--paper);
    overflow: hidden;
  }
  .calendar-title {
    position: absolute;
    left: 46px;
    top: 52px;
    font-family: "Arimo", Arial, sans-serif;
    font-weight: 700;
    color: var(--title-green);
    font-size: 35px;
    white-space: nowrap;
  }
  .calendar-title .month {
    color: var(--leaf-green);
    font-size: 48px;
    margin-left: 4px;
  }
  .brand-panel {
    position: absolute;
    left: 887px;
    top: 0;
    width: 281px;
    height: 186px;
    background: var(--white);
    z-index: 2;
    display: flex;
    align-items: center;
    justify-content: center;
    gap: 12px;
  }
  .brand-dot {
    width: 34px;
    height: 34px;
    border-radius: 50%;
    background: var(--leaf-green);
  }
  .brand-name {
    font-family: "Questrial", Arial, sans-serif;
    color: var(--leaf-green);
    font-size: 26px;
    letter-spacing: 1.5px;
  }
  .event-bar {
    position: absolute;
    left: 140px;
    right: 0;
    height: 28px;
    background: var(--sage);
    color: var(--white);
    font-family: "Roboto Condensed", "Arial Narrow", sans-serif;
    font-size: 20px;
    line-height: 28px;
    padding-left: 8px;
    white-space: nowrap;
    z-index: 1;
  }
  .date-leaf {
    position: absolute;
    left: 54px;
    width: 74px;
    height: 64px;
    background: var(--leaf-green);
    border-radius: 60% 60% 45% 45% / 70% 70% 35% 35%;
  }
  .date-number {
    position: absolute;
    left: 78px;
    width: 48px;
    font-family: "Arimo", Arial, sans-serif;
    font-weight: 700;
    font-size: 33px;
    line-height: 40px;
    color: var(--white);
    z-index: 3;
  }
  .site-footer {
    position: absolute;
    left: 0;
    right: 0;
    top: 824px;
    height: 35px;
    background: var(--leaf-green);
    color: var(--white);
    font-family: "Arimo", Arial, sans-serif;
    font-weight: 700;
    font-size: 28px;
    line-height: 35px;
    text-align: center;
  }
</style>
</head>
<body>
<main class="calendar-card">
  <h1 class="calendar-title">Dynamic Calendar for <span class="month">February 2014</span></h1>

  <div class="brand-panel">
    <span class="brand-dot"></span>
    <span class="brand-name">TORVESI HALL</span>
  </div>

  <!-- Date markers -->
  <div class="date-leaf" style="top:114px" role="img" aria-label="Green ginkgo leaf date marker"></div>
  <div class="date-number" style="top:126px">03</div>
  <div class="date-leaf" style="top:194px" role="img" aria-label="Green ginkgo leaf date marker"></div>
  <div class="date-number" style="top:206px">05</div>
  <div class="date-leaf" style="top:270px" role="img" aria-label="Green ginkgo leaf date marker"></div>
  <div class="date-number" style="top:282px">07</div>
  <div class="date-leaf" style="top:346px" role="img" aria-label="Green ginkgo leaf date marker"></div>
  <div class="date-number" style="top:358px">12</div>
  <div class="date-leaf" style="top:423px" role="img" aria-label="Green ginkgo leaf date marker"></div>
  <div class="date-number" style="top:435px">14</div>
  <div class="date-leaf" style="top:501px" role="img" aria-label="Green ginkgo leaf date marker"></div>
  <div class="date-number" style="top:513px">19</div>
  <div class="date-leaf" style="top:579px" role="img" aria-label="Green ginkgo leaf date marker"></div>
  <div class="date-number" style="top:591px">21</div>
  <div class="date-leaf" style="top:660px" role="img" aria-label="Green ginkgo leaf date marker"></div>
  <div class="date-number" style="top:672px">26</div>
  <div class="date-leaf" style="top:737px" role="img" aria-label="Green ginkgo leaf date marker"></div>
  <div class="date-number" style="top:749px">28</div>

  <!-- Events -->
  <div class="event-bar" style="top:122px">GROUP IV SESSION ( From: 09:00 am To 01:00 pm , With Dr. Maren Holloway )</div>
  <div class="event-bar" style="top:155px">GROUP ACUPUNCTURE ( From: 10:00 am To 12:00 pm , With Celia Marsh, LAc )</div>
  <div class="event-bar" style="top:203px">YOGA AFTER TRAUMA: RECLAIMING BODY AND MIND ( From: 09:30 am To10:30 am )</div>
  <div class="event-bar" style="top:235px">"HAPPY HOUR" GROUP ACUPUNCTURE ( From: 05:00 pm To 07:00 pm , With&nbsp; Dana Whitcombe, LAc )</div>
  <div class="event-bar" style="top:294px">FOOD STORY TRANSFORMATION PROGRAM ( From: 10:00 am To 12:00 pm )</div>
  <div class="event-bar" style="top:366px">YOGA AFTER TRAUMA: RECLAIMING BODY AND MIND ( From: 09:30 am To 10:30 am )</div>
  <div class="event-bar" style="top:438px">FOOD STORY TRANSFORMATION PROGRAM ( From: 10:00 am To 12:00 pm )</div>
  <div class="event-bar" style="top:522px">YOGA AFTER TRAUMA: RECLAIMING BODY AND MIND ( From: 09:30 am To 10:30 am )</div>
  <div class="event-bar" style="top:603px">FOOD STORY TRANSFORMATION PROGRAM ( From: 10:00 am To 12:00 pm )</div>
  <div class="event-bar" style="top:685px">YOGA AFTER TRAUMA: RECLAIMING BODY AND MIND SPIRIT ( From: 09:30 am To 10:30 am )</div>
  <div class="event-bar" style="top:766px">FOOD STORY TRANSFORMATION PROGRAM ( From: 10:00 am To 12:00 pm )</div>

  <footer class="site-footer">www.torvesihall.com</footer>
</main>
</body>
</html>
```